label bath salt on glass bottle

for our bath salts (Flavours Rose, Lavender, Lemongras, mountain herbs, Mint, Cashmere) we need a label in the size of 50mm height an 55mm wide.

Target Market(s)

Prestige stores

Font styles to use
Serif
Script

Colors

Designer to choose colors to be used in the design.

Requirements
Must have
• Name of the label:
• Headline: Badesalz (can be also written in two words) Bade Salz
• Describtion of the sel: Totes Meer (comes from Dead Sea)
• Name of the different fragrances:
• Rose
• Pfingstrose (Peony)
• Lemongras
• Alpenkräuter (mountain herbs)
• Minze (mint)
• Cashmere
• Lavendel (lavender)
Nice to have
• Made with love in Switzerland
• Logos:
• Use our LOGO in the attachment or just
• FENIVU
• Switzerland

```html
<!DOCTYPE html>
<html lang="de">
<head>
<meta charset="utf-8">
<title>FENIVU Bade Salz – Alpenkräuter</title>
<link rel="stylesheet" href="https://fonts.googleapis.com/css2?family=Cormorant+Garamond:ital,wght@1,500&family=Lobster&family=Montserrat:wght@400;500;600&display=swap">
<style>
  :root {
    --backdrop: #e8ebf0;
    --label-white: #fbfaf8;
    --gold: #c4a678;
    --gold-dark: #5e4a2c;
    --pink: #ec6f9c;
    --pink-light: #f08bb0;
    --cross: #ffffff;
    --ink-grey: #4f5052;
    --herb-green: #6fe07c;
    --pill-text: #ffffff;
  }
  * { box-sizing: border-box; margin: 0; padding: 0; }
  html, body { width: 1200px; height: 800px; overflow: hidden; }
  body { background: var(--backdrop); position: relative; }

  .label {
    position: absolute;
    left: 324px;
    top: 40px;
    width: 552px;
    height: 720px;
    overflow: hidden;
  }
  .label-top {
    position: absolute;
    inset: 0 0 auto 0;
    height: 257px;
    background: var(--label-white);
  }
  .brand-name {
    position: absolute;
    top: 74px;
    left: 0; right: 0;
    text-align: center;
    font-family: "Montserrat", sans-serif;
    font-weight: 500;
    font-size: 50px;
    letter-spacing: 4px;
    color: var(--gold);
  }
  .tagline {
    position: absolute;
    top: 204px;
    left: 0; right: 0;
    text-align: center;
    font-family: "Cormorant Garamond", serif;
    font-style: italic;
    font-weight: 500;
    font-size: 32px;
    letter-spacing: 1px;
    color: var(--gold);
  }
  .label-bottom {
    position: absolute;
    inset: 257px 0 0 0;
    background: linear-gradient(160deg, var(--pink-light) 0%, var(--pink) 45%, var(--pink) 100%);
  }
  .swiss-cross {
    position: absolute;
    left: 138px;
    top: 70px;
    width: 294px;
    height: 251px;
  }
  .product-title {
    position: absolute;
    top: 46px;
    left: 0; right: 0;
    text-align: center;
    font-family: "Lobster", cursive;
    font-weight: 400;
    font-size: 106px;
    line-height: 1;
    color: var(--gold);
    -webkit-text-stroke: 3px var(--gold-dark);
    paint-order: stroke fill;
  }
  .salt-origin {
    position: absolute;
    top: 150px;
    left: 0; right: 0;
    text-align: center;
    font-family: "Montserrat", sans-serif;
    font-weight: 400;
    font-size: 56px;
    line-height: 1.2;
    color: var(--ink-grey);
  }
  .fragrance-pill {
    position: absolute;
    left: 52px;
    top: 342px;
    width: 434px;
    height: 58px;
    border-radius: 29px;
    background: var(--herb-green);
    color: var(--pill-text);
    font-family: "Montserrat", sans-serif;
    font-weight: 500;
    font-size: 27px;
    display: flex;
    align-items: center;
    justify-content: center;
    letter-spacing: 0.5px;
  }
</style>
</head>
<body>
  <section class="label">
    <header class="label-top">
      <div class="brand-name">FENIVU</div>
      <div class="tagline">scents of calm</div>
    </header>
    <div class="label-bottom">
      <svg class="swiss-cross" viewBox="0 0 294 251" aria-hidden="true">
        <rect x="92" y="0" width="86" height="251" fill="var(--cross)"/>
        <rect x="0" y="80" width="294" height="95" fill="var(--cross)"/>
      </svg>
      <h1 class="product-title">Bade Salz</h1>
      <p class="salt-origin">Totes Meer</p>
      <div class="fragrance-pill">Alpenkrauter</div>
    </div>
  </section>
</body>
</html>
```